Business card design needed

Quiet Haven Network is a not-for- profit organisation which advocates for palliative care in the community and runs a good size volunteer program to the community. We also run day hospice centres, provide massage & podiatry to clients etc. Our current business cards are very old fashioned and a new look is timely to some positive changes bringing the organisation forward.
Updates

Hi everyone, Thank you all so much for submitting your very clever designs.  I will confer with my colleagues tomorrow and hopefully we can make a decision :)

Industry/Entity Type

Massage

Contact Information for Business Card

Miriam Coley
Operations Manager
T 02 6180 4392
M 0417552864
E Miriam@quiethavennet.org.au

Logo Text

Quiet Haven Network Inc

Logo styles of interest
Pictorial/Combination Logo
Requirements
Must have
• Our logo (I think I have attached it, contact me if it didn't work)

```html
<!DOCTYPE html>
<html lang="en">
<head>
<meta charset="utf-8">
<title>Quiet Haven Network – Business Card</title>
<link rel="stylesheet" href="https://fonts.googleapis.com/css2?family=Questrial&display=swap">
<style>
  :root {
    --page-bg: #f3f3f4;
    --card-bg: #ffffff;
    --magenta: #e012b4;
    --org-pink: #b0206e;
    --art-yellow: #f7e93a;
    --art-amber: #f2b233;
    --art-red: #e2421e;
  }
  * { box-sizing: border-box; margin: 0; padding: 0; }
  html, body {
    width: 1200px;
    height: 1000px;
    overflow: hidden;
    background: var(--page-bg);
  }
  .stage {
    position: relative;
    width: 1200px;
    height: 1000px;
  }
  .business-card {
    position: absolute;
    left: 100px;
    top: 200px;
    width: 1000px;
    height: 600px;
    background: var(--card-bg);
    border-radius: 28px;
    box-shadow: 0 10px 40px rgba(0, 0, 0, 0.08);
    overflow: hidden;
    font-family: "Questrial", "Century Gothic", sans-serif;
    color: var(--magenta);
  }
  .brand {
    position: absolute;
    left: 60px;
    top: 70px;
    display: flex;
    align-items: center;
    gap: 12px;
  }
  .brand-dot {
    width: 22px;
    height: 22px;
    border-radius: 50%;
    background: var(--org-pink);
  }
  .brand-name {
    font-size: 20px;
    color: var(--org-pink);
  }
  .feature-art {
    position: absolute;
    left: 600px;
    top: 50px;
    width: 360px;
    height: 400px;
    border-radius: 50%;
    background: radial-gradient(circle at 50% 45%,
      var(--art-amber) 0%,
      var(--art-yellow) 38%,
      rgba(247, 233, 58, 0.35) 62%,
      rgba(255, 255, 255, 0) 72%);
  }
  .person {
    position: absolute;
    right: 430px;
    top: 255px;
    text-align: right;
  }
  .person-name {
    font-size: 56px;
    font-weight: 400;
    line-height: 1.05;
  }
  .person-title {
    font-size: 32px;
    line-height: 1.2;
  }
  .contact-list {
    position: absolute;
    left: 540px;
    top: 440px;
    list-style: none;
    font-size: 22px;
    line-height: 1.5;
  }
</style>
</head>
<body>
  <main class="stage">
    <article class="business-card">
      <div class="brand">
        <span class="brand-dot"></span>
        <span class="brand-name">Quiet Haven Network Inc</span>
      </div>

      <div class="feature-art" role="img" aria-label="Large watercolour illustration area in yellow and amber tones"></div>

      <div class="person">
        <h1 class="person-name">Miriam Coley</h1>
        <p class="person-title">Operations Manager</p>
      </div>

      <ul class="contact-list">
        <li>Phone -02 6180 4392</li>
        <li>Mobile -0417552864</li>
        <li>E-mail -Miriam@quiethavennet.org.au</li>
      </ul>
    </article>
  </main>
</body>
</html>
```